Tulven Electrics Flyer Design Advertising

I am after an A5 Flyer design to help promote my electrical services business.
I would like to have information on what my business offers, photos of electrical work, and specials/deals for an amount of time.

Industry/Entity Type

Electrician

Font styles to use
Sans Serif

Colors
0292cd
33a6d7
85cae6
3176b5
333333
1b1b1b
ffffff
5c5c5c
474747

Requirements
Must have
• Specialising in New homes, renovations and commercial projects
• Contact details:
• ph. 0437 619 458
• email admin@tulvenelectrics.example.au
• facebook TulvenElectrics
• Specials/Deals:
• 10% off all electrical services
• or
• Free LED downlights on installation
• *Terms conditions apply
• ALL RESIDENTIAL & COMMERCIAL ELECTRICAL SERVICES
• - New Home installations
• - Commercial projects
• - Shop fit outs
• - Renovations
• - Smoke Detectors
• - Air Conditioning and Ceiling Fans
• - Garden Lighting
• - Oven and Cooktop Installations
• - Power Point installation
• - LED lighting upgrades
• - Security Lighting
• - Switchboard upgrades
• - Test and Tag
• - Commercial Property
• - General Electrical Maintenance

```html
<!DOCTYPE html>
<html lang="en">
<head>
<meta charset="utf-8">
<title>Tulven Electrics – Special Offers Flyer</title>
<link href="https://fonts.googleapis.com/css2?family=Roboto+Condensed:wght@300;400;700&family=Oswald:wght@300;400;600&display=swap" rel="stylesheet">
<style>
  :root{
    --blue:#0292cd;
    --blue-mid:#33a6d7;
    --blue-light:#85cae6;
    --blue-deep:#3176b5;
    --ink:#333333;
    --ink-dark:#1b1b1b;
    --white:#ffffff;
    --grey:#5c5c5c;
    --grey-dark:#474747;
  }
  html,body{margin:0;padding:0;overflow:hidden;background:var(--white);}
  .flyer{
    position:relative;width:847px;height:1200px;overflow:hidden;
    font-family:"Roboto Condensed",Arial,sans-serif;color:var(--white);
    background:var(--ink-dark);
  }
  .hero-photo{
    position:absolute;inset:0;
    background:
      radial-gradient(ellipse at 25% 72%, rgba(240,170,90,.45), transparent 40%),
      radial-gradient(ellipse at 70% 60%, rgba(133,202,230,.25), transparent 45%),
      linear-gradient(180deg,#4a5560 0%,#2c343b 35%,#3a3430 60%,#1b1b1b 100%);
  }
  .header-wash{
    position:absolute;left:0;top:0;width:847px;height:400px;
  }
  .interior-photo{
    position:absolute;left:0;top:0;width:560px;height:300px;
    background:linear-gradient(90deg,rgba(200,205,210,.55),rgba(255,255,255,0));
  }
  .brand{
    position:absolute;left:70px;top:62px;display:flex;align-items:center;gap:16px;
  }
  .brand-dot{width:60px;height:60px;border-radius:50%;background:var(--ink);}
  .brand-name{
    font-family:"Oswald",Arial,sans-serif;font-weight:600;font-size:40px;
    color:var(--ink);letter-spacing:1px;
  }
  .tagline{
    position:absolute;left:60px;top:205px;width:380px;
    font-size:17px;letter-spacing:2px;color:var(--grey);text-transform:uppercase;line-height:1.75;
  }
  .contacts{
    position:absolute;right:40px;top:22px;text-align:right;
    font-size:17px;color:var(--grey-dark);line-height:1;
  }
  .contact{display:flex;justify-content:flex-end;align-items:center;gap:14px;margin-bottom:22px;}
  .contact svg{width:24px;height:24px;flex:none;}
  .offers-title{
    position:absolute;left:0;width:847px;top:400px;text-align:center;
    font-family:"Oswald",Arial,sans-serif;font-weight:400;font-size:36px;letter-spacing:3px;
  }
  .offers-title::before,.offers-title::after{
    content:"";display:block;width:380px;height:2px;background:var(--white);margin:0 auto;
  }
  .offers-title::before{margin-bottom:6px}
  .offers-title::after{margin-top:6px}
  .deal-percent{
    position:absolute;left:135px;top:455px;
    font-family:"Oswald",Arial,sans-serif;font-weight:300;font-size:122px;line-height:1;
  }
  .deal-percent-note{
    position:absolute;left:375px;top:470px;
    font-family:"Oswald",Arial,sans-serif;font-weight:400;font-size:32px;line-height:1.2;letter-spacing:1px;
  }
  .deal-free-note{
    position:absolute;left:290px;top:610px;text-align:center;
    font-family:"Oswald",Arial,sans-serif;font-weight:400;font-size:32px;line-height:1.15;letter-spacing:1px;
  }
  .deal-free{
    position:absolute;left:540px;top:600px;
    font-family:"Oswald",Arial,sans-serif;font-weight:400;font-size:118px;line-height:1;letter-spacing:2px;
  }
  .services-band{position:absolute;left:0;top:748px;width:740px;height:84px;}
  .services-heading{
    position:absolute;left:120px;top:756px;color:var(--ink-dark);
    font-weight:700;font-size:28px;line-height:1.2;text-align:center;
  }
  .services{
    position:absolute;left:72px;top:862px;display:flex;gap:90px;
    font-size:22px;line-height:28px;list-style:none;margin:0;padding:0;
  }
  .services ul{list-style:none;margin:0;padding:0;}
  .offer-ends{
    position:absolute;left:495px;top:1128px;display:flex;align-items:center;gap:14px;
    font-family:"Oswald",Arial,sans-serif;font-size:24px;letter-spacing:1px;
  }
  .offer-ends-box{width:200px;height:40px;background:var(--white);}
</style>
</head>
<body>
<div class="flyer">
  <div class="hero-photo" role="img" aria-label="Modern home exterior lit up at dusk with glowing interior lights and surrounding trees"></div>

  <svg class="header-wash" viewBox="0 0 847 400" aria-hidden="true">
    <polygon points="0,0 847,0 847,240 0,385" fill="#ffffff"/>
    <polygon points="520,0 847,0 847,240 600,282" fill="#1b1b1b" opacity=".12"/>
    <line x1="0" y1="385" x2="847" y2="240" stroke="#0292cd" stroke-width="3"/>
  </svg>
  <div class="interior-photo" role="img" aria-label="Faded view of a bright modern kitchen interior with pendant lights"></div>

  <div class="brand">
    <span class="brand-dot"></span>
    <span class="brand-name">TULVEN ELECTRICS</span>
  </div>
  <p class="tagline">Specialising in new homes, renovations &amp; commercial projects</p>

  <div class="contacts">
    <div class="contact"><span>reid@tulvenelectrics.example.au</span>
      <svg viewBox="0 0 24 24"><circle cx="12" cy="12" r="12" fill="#333333"/><rect x="6" y="8" width="12" height="8" fill="none" stroke="#fff" stroke-width="1.5"/><polyline points="6,8 12,13 18,8" fill="none" stroke="#fff" stroke-width="1.5"/></svg></div>
    <div class="contact"><span>0437 619 458</span>
      <svg viewBox="0 0 24 24"><circle cx="12" cy="12" r="12" fill="#333333"/><path d="M8 6l2.5 0 1 3-1.5 1.2a8 8 0 0 0 3.8 3.8L15 12.5l3 1v2.5a1.5 1.5 0 0 1-1.5 1.5A10.5 10.5 0 0 1 6.5 7.5 1.5 1.5 0 0 1 8 6z" fill="#fff"/></svg></div>
    <div class="contact"><span>/TulvenElectrics</span>
      <svg viewBox="0 0 24 24"><rect width="24" height="24" rx="3" fill="#333333"/></svg></div>
  </div>

  <h2 class="offers-title" style="margin:0">SPECIAL OFFERS</h2>

  <div class="deal-percent">%10</div>
  <div class="deal-percent-note">OFF ANY<br>ELECTRICAL<br>WORK</div>

  <div class="deal-free-note">LED DOWNLIGHTS<br>ON<br>INSTALLATION</div>
  <div class="deal-free">FREE</div>

  <svg class="services-band" viewBox="0 0 740 84" aria-hidden="true">
    <polygon points="0,0 740,0 700,84 0,84" fill="#ffffff"/>
  </svg>
  <h3 class="services-heading" style="margin:0">ALL RESIDENTIAL &amp; COMMERCIAL<br>ELECTRICAL SERVICES</h3>

  <div class="services">
    <ul>
      <li>- New Home Installations</li>
      <li>- Shop Fit Outs</li>
      <li>- Renovations</li>
      <li>- Smoke Detectors</li>
      <li>- Air Conditioning &amp; Ceiling Fans</li>
      <li>- Garden Lighting</li>
      <li>- Oven &amp; Cooktop Installations</li>
    </ul>
    <ul>
      <li>- Power Point Installation</li>
      <li>- Led Lighting Upgrades</li>
      <li>- Security Lighting</li>
      <li>- Switchboard Upgrades</li>
      <li>- Test &amp; Tag</li>
      <li>- General Electrical Maintenance</li>
    </ul>
  </div>

  <div class="offer-ends"><span>OFFER ENDS:</span><span class="offer-ends-box"></span></div>
</div>
</body>
</html>
```